New Construction company looking for powerful bold logo. people see the logo, leaves an impression

We need a business card for our new company. We provide site work for commercial projects in South Texas. We clear land, excavation, run under ground utilities, concrete work, dirt work etc. We like the black card. I created a webpage www.tarn-vbuilders.com .... As I grow with projects I will put up pictures with video, and intro music. Want it look cool, bold, powerful, and slick looking. Creating 'TVB'....as my logo (possibly or if you have something you want to have fun with). Just have fun!!....thank you!

Dorian Pruett Business Manager Serving South Texas PO Box 4837 Robstown,TX. 78380 Mobile: 361-752-6083 www.tarn-vbuilders.com dorian@tarn-vbuilders.com you can put this anyway you see fit in your design and layout. thank you

Target Market(s)

General Contractors; Home Builders;

Industry/Entity Type

Construction

Contact Information for Business Card

I want the card to be black.

Font styles to use
Other font styles liked:
• Designer choice

Requirements
Must have
• Tarn-V Construction
• Site Work - Utilities/Concrete/Pad/Grading/Excavation (on the back side)
Nice to have
• Maybe TVB as the logo.....or just a symbol that would be TV.....and then construction to tie it togther...

```html
<!DOCTYPE html>
<html lang="en">
<head>
<meta charset="utf-8">
<title>Tarn-V Construction – Business Card</title>
<link rel="stylesheet" href="https://fonts.googleapis.com/css2?family=Play:wght@400;700&family=Oswald:wght@500&family=Arimo:wght@400&display=swap">
<style>
  :root {
    --backdrop: #5b4335;
    --card-white: #fbfbfb;
    --card-black: #000000;
    --brand-yellow: #fccb00;
    --ink: #111111;
    --ink-soft: #555555;
    --divider: #6a6a6a;
    --wordmark-grey: #7a7a7c;
    --service-white: #ffffff;
  }
  * { box-sizing: border-box; margin: 0; padding: 0; }
  html, body {
    width: 1200px; height: 1000px; overflow: hidden;
    background: var(--backdrop);
  }
  .card {
    position: absolute; left: 266px; width: 667px; height: 381px;
    box-shadow: 2px 4px 8px rgba(0,0,0,.35);
  }
  /* Front */
  .card-front {
    top: 102px;
    background: radial-gradient(ellipse at 50% 45%, #ffffff 0%, var(--card-white) 55%, #ededed 100%);
  }
  .front-mark {
    position: absolute; left: 112px; top: 150px;
    display: flex; align-items: center; gap: 10px;
  }
  .front-mark .mark-name {
    font-family: "Oswald", sans-serif; font-weight: 500;
    font-size: 92px; line-height: 1; color: var(--ink); letter-spacing: 1px;
  }
  .front-mark .mark-square {
    width: 18px; height: 18px; background: var(--brand-yellow);
  }
  .front-divider {
    position: absolute; left: 331px; top: 71px; width: 3px; height: 240px;
    background: var(--divider);
  }
  .contact-block {
    position: absolute; left: 345px; top: 134px;
    font-family: "Play", sans-serif;
  }
  .person-name { font-size: 21px; color: var(--ink); line-height: 26px; }
  .person-role { font-size: 14px; color: var(--ink-soft); line-height: 18px; }
  .contact-list { list-style: none; margin-top: 22px; }
  .contact-list li {
    font-size: 15px; line-height: 19.5px; color: var(--ink-soft);
    display: flex;
  }
  .contact-list .label { color: var(--brand-yellow); width: 24px; }
  .front-band {
    position: absolute; left: 0; bottom: 0; width: 100%; height: 15px; display: flex;
  }
  .front-band .band-yellow { width: 331px; background: var(--brand-yellow); }
  .front-band .band-gap { width: 4px; background: #ffffff; }
  .front-band .band-black { flex: 1; background: var(--card-black); }
  /* Back */
  .card-back { top: 520px; background: var(--card-black); }
  .back-wordmark {
    position: absolute; left: 0; right: 0; top: 158px;
    display: flex; justify-content: center; align-items: center; gap: 14px;
  }
  .back-wordmark .mark-square {
    width: 16px; height: 16px; background: var(--brand-yellow);
  }
  .back-wordmark .mark-name {
    font-family: "Oswald", sans-serif; font-weight: 500;
    font-size: 52px; line-height: 1; color: var(--wordmark-grey); letter-spacing: 1px;
  }
  .service-list {
    position: absolute; left: 0; right: 0; top: 258px;
    list-style: none; display: flex; justify-content: center; gap: 14px;
    font-family: "Arimo", sans-serif; font-size: 18px; color: var(--service-white);
  }
  .service-list li { display: flex; align-items: center; gap: 7px; }
  .service-list li::before {
    content: ""; width: 6px; height: 6px; border-radius: 50%;
    background: var(--brand-yellow);
  }
</style>
</head>
<body>
  <section class="card card-front" aria-label="Business card front">
    <div class="front-mark">
      <span class="mark-name">TV</span>
      <span class="mark-square"></span>
    </div>
    <div class="front-divider"></div>
    <div class="contact-block">
      <p class="person-name">Person Name</p>
      <p class="person-role">Designation</p>
      <ul class="contact-list">
        <li><span class="label">P:</span>123 456 7890</li>
        <li><span class="label">F:</span>123 456 7890</li>
        <li><span class="label">E:</span>info@abcdef.com</li>
        <li><span class="label">W:</span>www.abcdef.com</li>
      </ul>
    </div>
    <div class="front-band">
      <span class="band-yellow"></span><span class="band-gap"></span><span class="band-black"></span>
    </div>
  </section>

  <section class="card card-back" aria-label="Business card back">
    <div class="back-wordmark">
      <span class="mark-square"></span>
      <span class="mark-name">TARN-V CONSTRUCTION</span>
    </div>
    <ul class="service-list">
      <li>Utilities</li>
      <li>Concrete</li>
      <li>Pad</li>
      <li>Grading</li>
      <li>Excavation</li>
    </ul>
  </section>
</body>
</html>
```